Modern and Improved business card design for Family Dental Practice

We have 2 sets of logo we have designed and now just need a business card layout and design for the office. Colors are on the logo. We can choose which logo we want to go with . The font can be changed to whatever seems modern and relevant. We are family dental office that has been open for over 15 years in South Austin Texas.

Target Market(s)

Handout Business cards to referrals and specialists

Industry/Entity Type

Dental

Contact Information for Business Card

We need address, phone, website and email address. 4870 North Loop Rd Suite 208 , Austin,Texas 78651....phone: 512-480-7319.....email- info@maplebrookdental-example.com....website - MapleBrookDental-example.com

Font styles to use
Serif
Decorative

Requirements
Must have
• my logo. We have 2 logos, but we can use just one or if we can incorporate one on one side and the other on the other side.
Nice to have
• Really just need a modern look and clean that incorporates the logo and colors .

```html
<!DOCTYPE html>
<html lang="en">
<head>
<meta charset="utf-8">
<title>Maple Brook Family Dentistry – Business Cards</title>
<link rel="stylesheet" href="https://fonts.googleapis.com/css2?family=Josefin+Sans:wght@300;400&family=Arimo:wght@400;700&display=swap">
<style>
  :root {
    --backdrop: #e6e6e3;
    --card-black: #1c1c1c;
    --card-white: #f7f7f5;
    --brand-green: #0b7a0f;
    --brand-green-dark: #066309;
    --ink: #1a1a1a;
    --on-green: #ffffff;
  }
  * { box-sizing: border-box; margin: 0; padding: 0; }
  html, body {
    width: 1200px;
    height: 768px;
    overflow: hidden;
    background: var(--backdrop);
  }
  .stage {
    position: relative;
    width: 1200px;
    height: 768px;
  }
  .card {
    position: absolute;
    top: 234px;
    width: 525px;
    height: 300px;
    border-radius: 3px;
    overflow: hidden;
    box-shadow: 0 10px 28px rgba(0,0,0,0.18);
  }

  /* Back side */
  .card-back {
    left: 45px;
    background: var(--card-black);
    border-bottom: 3px solid var(--brand-green-dark);
    display: flex;
    align-items: center;
    justify-content: center;
    gap: 22px;
  }
  .brand-dot {
    width: 64px;
    height: 64px;
    border-radius: 50%;
    background: var(--brand-green);
    flex: none;
  }
  .brand-name {
    font-family: "Josefin Sans", sans-serif;
    font-weight: 400;
    text-transform: uppercase;
    line-height: 1;
  }
  .card-back .brand-name { color: var(--on-green); }
  .brand-name .line-main {
    display: block;
    font-size: 40px;
    letter-spacing: 1px;
  }
  .brand-name .line-sub {
    display: block;
    font-size: 14px;
    letter-spacing: 3px;
    margin-top: 8px;
  }

  /* Front side */
  .card-front {
    left: 630px;
    background: var(--card-white);
  }
  .front-top {
    height: 138px;
    padding: 26px 0 0 42px;
  }
  .card-front .brand-name { color: var(--ink); }
  .card-front .brand-name .line-main { font-size: 34px; }
  .card-front .brand-name .line-sub { font-size: 13px; letter-spacing: 2.5px; }
  .front-band {
    position: absolute;
    left: 0;
    right: 0;
    bottom: 0;
    height: 162px;
    background: var(--brand-green);
    padding: 20px 0 0 42px;
    color: var(--on-green);
    font-family: "Arimo", sans-serif;
  }
  .person-name {
    font-size: 19px;
    font-weight: 700;
    line-height: 1.1;
  }
  .person-title {
    font-size: 13px;
    margin-top: 2px;
  }
  .address {
    font-size: 13px;
    line-height: 1.3;
    margin-top: 10px;
  }
  .contact-list {
    list-style: none;
    margin-top: 6px;
    font-size: 13px;
    line-height: 1.35;
  }
  .contact-list li {
    display: flex;
    align-items: center;
    gap: 8px;
  }
  .contact-list svg {
    width: 11px;
    height: 11px;
    flex: none;
  }
</style>
</head>
<body>
<main class="stage">

  <section class="card card-back" aria-label="Card back">
    <span class="brand-dot" aria-hidden="true"></span>
    <h1 class="brand-name">
      <span class="line-main">Maple Brook</span>
      <span class="line-sub">Family Dentistry</span>
    </h1>
  </section>

  <section class="card card-front" aria-label="Card front">
    <header class="front-top">
      <h2 class="brand-name">
        <span class="line-main">Maple Brook</span>
        <span class="line-sub">Family Dentistry</span>
      </h2>
    </header>
    <div class="front-band">
      <p class="person-name">Daniel Whitford</p>
      <p class="person-title">Managing Director</p>
      <p class="address">4870 North Loop Rd, Suite 208<br>Austin, Texas 78651</p>
      <ul class="contact-list">
        <li>
          <svg viewBox="0 0 12 12" aria-hidden="true"><path d="M3 1 L5 3.5 L4 5 Q5 7 7 8 L8.5 7 L11 9 L9.5 11 Q4 10.5 1 3 Z" fill="#fff"/></svg>
          512-480-7319
        </li>
        <li>
          <svg viewBox="0 0 12 12" aria-hidden="true"><rect x="0.5" y="2" width="11" height="8" fill="#fff"/><path d="M0.5 2 L6 6.5 L11.5 2" fill="none" stroke="#0b7a0f" stroke-width="1"/></svg>
          info@maplebrookdental-example.com
        </li>
        <li>
          <svg viewBox="0 0 12 12" aria-hidden="true"><circle cx="6" cy="6" r="5.3" fill="#fff"/><path d="M0.7 6 H11.3 M6 0.7 Q3 6 6 11.3 M6 0.7 Q9 6 6 11.3" fill="none" stroke="#0b7a0f" stroke-width="0.8"/></svg>
          www.MapleBrookDental-example.com
        </li>
      </ul>
    </div>
  </section>

</main>
</body>
</html>
```